Roof Plumbing Company needs simple, modern business card using the attached logo and below details:

Glen Marwick
Kestrel Roofing Pty Ltd
ABN: 58 217 934 062
Phone: 0417 286 503
Email: kestrelroofing@mailvista.com
Website: kestrelroofing.com.au

For all of your metal roof plumbing requirements contact Kestrel Roofing for an obligation free quote - no job too big or to small!

Industry/Entity Type

Business

Contact Information for Business Card

Glen Marwick
Kestrel Roofing Pty Ltd
ABN 58 217 934 062
0417 286 503
kestrelroofing@mailvista.com
kestrelroofing.com.au

Requirements
Must have
• Bright eye catching design, professional look

```html
<!DOCTYPE html>
<html lang="en">
<head>
<meta charset="utf-8">
<title>Kestrel Roofing Business Card</title>
<link rel="stylesheet" href="https://fonts.googleapis.com/css2?family=Lato:wght@400;700;900&display=swap">
<style>
  :root {
    --bg: #e6e6e6;
    --card: #ffffff;
    --brand-red: #9b1b1e;
    --brand-red-deep: #86161a;
    --steel: #4a4a4a;
    --ink: #333333;
  }
  * { margin: 0; padding: 0; box-sizing: border-box; }
  html, body { width: 1200px; height: 1086px; overflow: hidden; background: var(--bg); }
  body { position: relative; font-family: "Lato", Arial, sans-serif; color: var(--ink); }

  .card {
    position: absolute; left: 254px; width: 677px; height: 386px;
    background: var(--card); border-radius: 8px; overflow: hidden;
  }
  .card--front { top: 126px; }
  .card--back { top: 587px; }

  .brand-mark { position: absolute; display: flex; align-items: center; gap: 12px; }
  .brand-mark__square { width: 22px; height: 22px; background: var(--brand-red); flex: none; }
  .brand-mark__name {
    font-weight: 900; color: var(--brand-red); font-size: 30px; line-height: 1.05;
    text-transform: uppercase; letter-spacing: 1px;
  }
  .card--front .brand-mark { left: 396px; top: 78px; }
  .card--back .brand-mark { left: 0; right: 0; top: 160px; justify-content: center; }
  .card--back .brand-mark__name { font-size: 34px; }

  .name-tab {
    position: absolute; left: 0; top: 222px; width: 18px; height: 46px;
    background: var(--brand-red); border-radius: 0 6px 6px 0;
  }
  .holder-name {
    position: absolute; left: 32px; top: 218px;
    font-weight: 700; font-size: 26px; color: var(--brand-red); letter-spacing: -0.3px;
  }
  .holder-abn { position: absolute; left: 32px; top: 246px; font-size: 15px; color: var(--ink); }

  .contact { position: absolute; left: 32px; display: flex; align-items: center; gap: 12px; font-size: 21px; }
  .contact svg { width: 24px; height: 20px; flex: none; }
  .contact--phone { top: 304px; }
  .contact--email { top: 331px; font-size: 20px; }

  .website { position: absolute; right: 33px; top: 329px; font-size: 20px; color: var(--ink); }
  .website__domain { color: var(--brand-red); }

  .tagline {
    position: absolute; left: 60px; right: 60px; top: 303px;
    text-align: center; font-size: 16.5px; line-height: 20px; color: var(--ink);
  }
  .footer-band { position: absolute; left: 0; bottom: 0; width: 677px; height: 30px; }
  .footer-url {
    position: absolute; left: 0; right: 0; bottom: 4px; text-align: center;
    color: #ffffff; font-size: 19px;
  }
</style>
</head>
<body>
  <section class="card card--front">
    <div class="brand-mark">
      <span class="brand-mark__square"></span>
      <span class="brand-mark__name">Kestrel Roofing<br>Pty Ltd</span>
    </div>

    <span class="name-tab"></span>
    <h1 class="holder-name">Glen Marwick</h1>
    <p class="holder-abn">ABN: 58 217 934 062</p>

    <p class="contact contact--phone">
      <svg viewBox="0 0 24 20" aria-hidden="true">
        <path d="M2 6c0-3 5-4 10-4s10 1 10 4v2h-5V6H7v2H2z" fill="#9b1b1e"/>
        <path d="M6 9h12l3 9H3z" fill="#9b1b1e"/>
        <circle cx="12" cy="13" r="2.5" fill="#fff"/>
      </svg>
      0417 286 503
    </p>
    <p class="contact contact--email">
      <svg viewBox="0 0 24 20" aria-hidden="true">
        <rect x="1" y="2" width="22" height="16" fill="#9b1b1e"/>
        <path d="M2 3l10 8 10-8M2 17l8-7M22 17l-8-7" stroke="#fff" stroke-width="1.5" fill="none"/>
      </svg>
      kestrelroofing@mailvista.com
    </p>

    <p class="website"><span class="website__domain">kestrelroofing</span>.com.au</p>
  </section>

  <section class="card card--back">
    <div class="brand-mark">
      <span class="brand-mark__square"></span>
      <span class="brand-mark__name">Kestrel Roofing Pty Ltd</span>
    </div>

    <p class="tagline">For all of your metal roof plumbing requirements contact Kestrel Roofing for<br>an obligation free quote - no job too big or to small!</p>

    <svg class="footer-band" viewBox="0 0 677 30" aria-hidden="true">
      <rect x="0" y="5" width="677" height="9" fill="var(--steel)"/>
      <rect x="0" y="14" width="677" height="16" fill="var(--brand-red)"/>
      <path d="M206 16 L222 2 L464 2 L480 16 Z" fill="#ffffff"/>
      <path d="M212 17 L226 4 L460 4 L474 17 Z" fill="var(--brand-red-deep)"/>
      <rect x="0" y="15" width="677" height="15" fill="var(--brand-red)"/>
      <path d="M212 17 L226 4 L460 4 L474 17 Z" fill="var(--brand-red)"/>
    </svg>
    <p class="footer-url">kestrelroofing.com.au</p>
  </section>
</body>
</html>
```